Redesign Gearcrate.co.uk website for Film,Tv & Photo Industries.

www.gearcrate.co.uk needs a major redesign and new fresh look.
We will be using Quillbrook V1 software and have a company that will do all the coding etc etc.

The website is for people who work in the film, tv and photographic industries and are looking to buy bags and cases for their equipment.
About 14 different Manufacturers will be featured.
Just need a modern home page, everything else will follow this design.
Updates

Hi All, I have altered the description of the project , not that much has altered just giving more info out. regards Rob Calder.

Hi Everyone, I have just uploaded a new logo for the www.gearcrate.co.uk website. regards Rob Calder.

Final logo has been uploaded. Regards Rob.

Reason: Even though there are many good designs a lot of them are the same. I would like to see even more of a modern design even using flat colours that don't follow the colour of the new logo regards Rob.

Having seen many very good designs I would like to see different designs using FLAT colours which are modern . You don't have to stick to the colours of the logo as i can change the red in the logo to match the colour of the website. regards Rob Calder.

Target Market(s)

Artistic People who work in Film , TV and photographic Industries. Photographers, cameramen, Production Companies who need to protect their equipment.
Both Pro and Amateur.

Industry/Entity Type

Software

Requirements
Must have
• open minded
Nice to have
• Modern Look

```html
<!DOCTYPE html>
<html lang="en">
<head>
<meta charset="utf-8">
<title>Gearcrate – Cases and Bags for Film, TV &amp; Photo</title>
<link href="https://fonts.googleapis.com/css2?family=Roboto:ital,wght@0,400;0,500;0,700;1,300;1,400&family=Roboto+Condensed:wght@400;700&family=Open+Sans:wght@400;600;700&display=swap" rel="stylesheet">
<style>
:root{
  --red:#9c1214;
  --red-bright:#c61f22;
  --ink:#2b2b2b;
  --muted:#8a8a8a;
  --page:#f4f4f2;
  --white:#ffffff;
  --line:#e2e2df;
  --ribbon-grey:#e6e6e3;
  --dark-btn:#2a2a2a;
}
*{box-sizing:border-box;margin:0;padding:0}
html,body{width:1200px;height:2365px;overflow:hidden}
body{background:var(--page);font-family:"Open Sans",Arial,sans-serif;color:var(--ink);position:relative}
.abs{position:absolute}

/* header */
.site-header{position:absolute;left:0;top:0;width:1200px;height:76px;background:#f7f7f5}
.brand{left:108px;top:14px;display:flex;align-items:center;gap:10px}
.brand-mark{width:34px;height:34px;border-radius:50%;background:var(--red)}
.brand-name{font-family:"Roboto Condensed",sans-serif;font-weight:700;font-size:38px;color:var(--red);letter-spacing:.5px}
.search{left:374px;top:19px;width:459px;height:36px;display:flex;border:1px solid #dcdcd8;background:var(--white)}
.search-scope{width:70px;background:#ededeb;font-size:12px;color:#999;display:flex;align-items:center;justify-content:center}
.search-input{flex:1;font-size:13px;color:#888;display:flex;align-items:center;padding-left:8px}
.search-btn{width:84px;background:var(--red);color:var(--white);font-family:"Roboto",sans-serif;font-weight:700;font-size:12px;letter-spacing:.5px;display:flex;align-items:center;justify-content:center}
.account-nav{left:872px;top:26px;display:flex;align-items:center;gap:22px;font-family:"Roboto",sans-serif;font-size:14px;color:var(--red)}
.basket{display:flex;align-items:center;gap:10px}
.basket-count{width:26px;height:26px;border-radius:50%;background:#e4e4e1;color:#555;font-size:12px;display:flex;align-items:center;justify-content:center}

/* hero */
.hero{left:0;top:76px;width:1200px;height:574px;background:linear-gradient(100deg,#e9eef2 0%,#c9d3dc 28%,#5d7c9c 42%,#dfe4e8 60%,#f1f1f1 80%,#cfd3d6 100%)}
.hero-panel{left:710px;top:218px;width:375px;height:247px;background:rgba(45,45,45,.82);padding:20px 26px}
.hero-kicker{font-family:"Roboto",sans-serif;font-style:italic;font-weight:300;font-size:33px;line-height:43px;color:var(--white)}
.hero-title{font-family:"Roboto",sans-serif;font-weight:500;font-size:47px;line-height:56px;color:var(--white);margin-top:2px}
.hero-cta{display:inline-block;margin-top:14px;background:var(--red-bright);color:var(--white);font-family:"Roboto",sans-serif;font-weight:500;font-size:21px;padding:11px 48px 12px}
.slider-dots{left:1019px;top:616px;display:flex;gap:4px}
.slider-dots span{width:11px;height:11px;background:#9a9a9a}
.slider-dots span.active{background:var(--red)}

/* explore */
.section-title{left:82px;top:690px;width:1038px;height:60px}
.section-title-text{left:0;top:0;width:1038px;height:60px;display:flex;align-items:center;justify-content:center;padding-right:120px;font-family:"Roboto",sans-serif;font-size:30px;color:#444}
.recent-badge{left:940px;top:656px;width:148px;height:148px;border-radius:50%;background:var(--red-bright);border:5px solid var(--white);box-shadow:0 0 0 2px #d4d4d4;color:var(--white);text-align:center;font-family:"Roboto Condensed",sans-serif;padding-top:30px}
.recent-badge .sm{font-size:17px;line-height:17px}
.recent-badge .lg{font-weight:700;font-size:30px;line-height:29px}

.showcase-card{top:780px;width:313px;height:363px;background:var(--white)}
.showcase-image{width:313px;height:310px}
.showcase-label{height:53px;display:flex;align-items:center;justify-content:center;font-family:"Roboto Condensed",sans-serif;font-size:19px;color:#222}

/* categories */
.browse-ribbon{left:370px;top:1192px;width:460px;height:48px}
.browse-text{left:370px;top:1192px;width:460px;height:48px;display:flex;align-items:center;justify-content:center;font-family:"Roboto Condensed",sans-serif;font-size:21px;color:var(--white)}
.tab-bar{left:110px;top:1266px;width:978px;height:76px;background:var(--white);border:1px solid #ececea;display:flex;align-items:center;padding-left:24px;font-family:"Roboto Condensed",sans-serif;font-size:19px;color:var(--red)}
.tab{padding:0 17px;height:76px;display:flex;align-items:center}
.tab.active{background:#ececea;color:#333}

.product{width:180px;text-align:center}
.product-image{margin:0 auto;height:137px;display:flex;align-items:center;justify-content:center}
.product-name{margin-top:14px;font-size:13px;color:#333}
.product-price{margin-top:3px;font-size:15px;font-weight:700;color:var(--red)}
.product-btn{margin:6px auto 0;width:110px;height:28px;background:var(--dark-btn);color:var(--white);font-size:12px;display:flex;align-items:center;justify-content:center;gap:8px}
.product-btn.hover{background:var(--red)}
.product-btn .arrow{color:var(--red-bright);font-weight:700}
.product-btn.hover .arrow{color:var(--white)}

/* featured */
.divider{left:0;width:1200px;height:1px;background:var(--line)}
.featured-ribbon{left:478px;top:1910px;width:244px;height:44px}
.featured-text{left:478px;top:1910px;width:244px;height:44px;display:flex;align-items:center;justify-content:center;font-family:"Roboto",sans-serif;font-size:20px;color:#555}
.press-badge{top:1984px;width:120px;height:52px;background:var(--white);border:1px solid #e6e6e3;display:flex;align-items:center;justify-content:center}
.press-badge span{width:84px;height:14px;background:#cfcfcc}

/* footer */
.footer-col{top:2108px}
.footer-col h4{font-family:"Open Sans",sans-serif;font-weight:600;font-size:15px;color:#444;margin-bottom:8px}
.footer-col li{list-style:none;font-size:12.5px;line-height:20px;color:#8a8a8a}
.subscribe-input{left:689px;top:2145px;width:271px;height:38px;border:1px solid #d8d8d5;background:var(--white);font-size:13px;color:#777;display:flex;align-items:center;padding-left:10px}
.subscribe-btn{left:971px;top:2145px;width:117px;height:38px;background:var(--red);color:var(--white);font-family:"Roboto",sans-serif;font-weight:700;font-size:14px;letter-spacing:.5px;display:flex;align-items:center;justify-content:center}
.social{left:109px;top:2258px;display:flex;gap:9px}
.social span{width:38px;height:38px;border-radius:3px}
.payments{left:773px;top:2224px;width:315px;height:82px;border:1px solid #d8d8d5;border-radius:6px;background:var(--white);display:flex;flex-direction:column;align-items:center;justify-content:center;gap:8px}
.payments .top{width:80px;height:12px;background:#c7d2e3;border-radius:2px}
.payments .cards{display:flex;gap:6px}
.payments .cards span{width:64px;height:40px;border-radius:4px;border:1px solid #e0e0e0}
.copyright{left:0;top:2330px;width:1200px;text-align:center;font-size:12px;color:#999}
</style>
</head>
<body>

<header class="site-header">
  <div class="abs brand"><span class="brand-mark"></span><span class="brand-name">Gearcrate</span></div>
  <div class="abs search">
    <div class="search-scope">Items →</div>
    <div class="search-input">...in Gearcrate</div>
    <div class="search-btn">SEARCH</div>
  </div>
  <nav class="abs account-nav">
    <span>Sign in</span><span>Register</span>
    <span class="basket">Basket <span class="basket-count">0</span></span>
  </nav>
</header>

<section class="abs hero" role="img" aria-label="Photo of a smiling photographer in glasses holding a DSLR camera at a bright desk with a monitor"></section>
<div class="abs hero-panel">
  <div class="hero-kicker">Everything you Need<br>for your</div>
  <div class="hero-title">NEW CAMERA</div>
  <span class="hero-cta">Shop Products</span>
</div>
<div class="abs slider-dots"><span></span><span class="active"></span><span></span><span></span></div>

<svg class="abs section-title" viewBox="0 0 1038 60" aria-hidden="true">
  <polygon points="0,0 1038,0 1010,30 1038,60 0,60 28,30" fill="#e6e6e3"/>
</svg>
<div class="abs section-title"><div class="abs section-title-text">Explore some of the great products at Gearcrate...</div></div>
<div class="abs recent-badge">
  <div class="sm">see our</div>
  <div class="lg">RECENTLY<br>LISTED</div>
  <div class="sm">items</div>
</div>

<article class="abs showcase-card" style="left:110px">
  <div class="showcase-image" role="img" aria-label="Photo of a collection of camera lenses and filters on a light grey background" style="background:radial-gradient(ellipse at 50% 55%,#3a3a3a 0%,#6b6b6b 28%,#e4e4e1 52%)"></div>
  <div class="showcase-label">FEATURED PRODUCTS</div>
</article>
<article class="abs showcase-card" style="left:445px">
  <div class="showcase-image" role="img" aria-label="Photo of a film studio set with cameras, lights and tall windows" style="background:linear-gradient(160deg,#5a4a4a 0%,#9aa9c2 35%,#2f2c30 70%,#4a3f3c 100%)"></div>
  <div class="showcase-label">PRODUCTION COMPANIES</div>
</article>
<article class="abs showcase-card" style="left:777px">
  <div class="showcase-image" role="img" aria-label="Photo of a photographer with a backpack shooting a sunset over mountains" style="background:linear-gradient(180deg,#f2c44a 0%,#e79a3a 45%,#9b5a2a 75%,#4a2a1a 100%)"></div>
  <div class="showcase-label">TV &amp; PHOTOGRAPHIC INDUSTRIES</div>
</article>

<svg class="abs browse-ribbon" viewBox="0 0 460 48" aria-hidden="true">
  <polygon points="0,6 22,6 22,42 0,42 12,24" fill="#7a0e10"/>
  <polygon points="460,6 438,6 438,42 460,42 448,24" fill="#7a0e10"/>
  <rect x="14" y="2" width="432" height="40" fill="#a51416"/>
</svg>
<div class="abs browse-text">OR BROWSE THROUGH OUR CATEGORIES...</div>

<nav class="abs tab-bar">
  <span class="tab active">Broadcast</span>
  <span class="tab">Photography</span>
  <span class="tab">Information</span>
  <span class="tab">Production Accessories</span>
  <span class="tab">Film Production Accessories</span>
  <span class="tab">Other Products</span>
</nav>

<!-- product grid row 1 -->
<div class="abs product" style="left:110px;top:1369px">
  <div class="product-image"><div role="img" aria-label="Black camera bag" style="width:82px;height:130px;border-radius:12px;background:linear-gradient(90deg,#111,#3a3a3a,#111)"></div></div>
  <div class="product-name">Ed ut perspiciatis unde</div><div class="product-price">£111.22</div>
  <div class="product-btn">View Details <span class="arrow">›</span></div>
</div>
<div class="abs product" style="left:304px;top:1369px">
  <div class="product-image"><div role="img" aria-label="Blue padded camera bag with equipment inside" style="width:130px;height:100px;border-radius:10px;background:linear-gradient(180deg,#3a55b0,#22357a)"></div></div>
  <div class="product-name">Ed ut perspiciatis unde</div><div class="product-price">£111.22</div>
  <div class="product-btn hover">View Details <span class="arrow">›</span></div>
</div>
<div class="abs product" style="left:506px;top:1369px">
  <div class="product-image"><div role="img" aria-label="Silver hard case with a broadcast camera on top" style="width:116px;height:110px;border-radius:6px;background:linear-gradient(180deg,#444 0%,#444 30%,#b9b9b6 30%,#8e8e8b 100%)"></div></div>
  <div class="product-name">Ed ut perspiciatis unde</div><div class="product-price">£111.22</div>
  <div class="product-btn">View Details <span class="arrow">›</span></div>
</div>
<div class="abs product" style="left:705px;top:1369px">
  <div class="product-image"><div role="img" aria-label="Studio lighting kit with umbrella and softboxes" style="width:130px;height:110px;background:radial-gradient(circle at 35% 40%,#fff 0%,#ddd 40%,#f4f4f2 70%)"></div></div>
  <div class="product-name">Ed ut perspiciatis unde</div><div class="product-price">£111.22</div>
  <div class="product-btn">View Details <span class="arrow">›</span></div>
</div>
<div class="abs product" style="left:903px;top:1369px">
  <div class="product-image"><div role="img" aria-label="Black professional camcorder" style="width:118px;height:76px;border-radius:8px;background:linear-gradient(180deg,#3a3a3a,#0f0f0f)"></div></div>
  <div class="product-name">Ed ut perspiciatis unde</div><div class="product-price">£111.22</div>
  <div class="product-btn">View Details <span class="arrow">›</span></div>
</div>

<!-- product grid row 2 -->
<div class="abs product" style="left:110px;top:1613px">
  <div class="product-image"><div role="img" aria-label="Black camera bag" style="width:82px;height:130px;border-radius:12px;background:linear-gradient(90deg,#111,#3a3a3a,#111)"></div></div>
  <div class="product-name">Ed ut perspiciatis unde</div><div class="product-price">£111.22</div>
  <div class="product-btn">View Details <span class="arrow">›</span></div>
</div>
<div class="abs product" style="left:304px;top:1613px">
  <div class="product-image"><div role="img" aria-label="Blue padded camera bag with equipment inside" style="width:130px;height:100px;border-radius:10px;background:linear-gradient(180deg,#3a55b0,#22357a)"></div></div>
  <div class="product-name">Ed ut perspiciatis unde</div><div class="product-price">£111.22</div>
  <div class="product-btn">View Details <span class="arrow">›</span></div>
</div>
<div class="abs product" style="left:506px;top:1613px">
  <div class="product-image"><div role="img" aria-label="Silver hard case with a broadcast camera on top" style="width:116px;height:110px;border-radius:6px;background:linear-gradient(180deg,#444 0%,#444 30%,#b9b9b6 30%,#8e8e8b 100%)"></div></div>
  <div class="product-name">Ed ut perspiciatis unde</div><div class="product-price">£111.22</div>
  <div class="product-btn">View Details <span class="arrow">›</span></div>
</div>
<div class="abs product" style="left:705px;top:1613px">
  <div class="product-image"><div role="img" aria-label="Studio lighting kit with umbrella and softboxes" style="width:130px;height:110px;background:radial-gradient(circle at 35% 40%,#fff 0%,#ddd 40%,#f4f4f2 70%)"></div></div>
  <div class="product-name">Ed ut perspiciatis unde</div><div class="product-price">£111.22</div>
  <div class="product-btn">View Details <span class="arrow">›</span></div>
</div>
<div class="abs product" style="left:903px;top:1613px">
  <div class="product-image"><div role="img" aria-label="Black professional camcorder" style="width:118px;height:76px;border-radius:8px;background:linear-gradient(180deg,#3a3a3a,#0f0f0f)"></div></div>
  <div class="product-name">Ed ut perspiciatis unde</div><div class="product-price">£111.22</div>
  <div class="product-btn">View Details <span class="arrow">›</span></div>
</div>

<div class="abs divider" style="top:1873px"></div>
<svg class="abs featured-ribbon" viewBox="0 0 244 44" aria-hidden="true">
  <polygon points="0,0 244,0 228,22 244,44 0,44 16,22" fill="#e6e6e3"/>
</svg>
<div class="abs featured-text">Featured in...</div>
<div class="abs press-badge" style="left:128px"><span></span></div>
<div class="abs press-badge" style="left:264px"><span></span></div>
<div class="abs press-badge" style="left:400px"><span></span></div>
<div class="abs press-badge" style="left:536px"><span></span></div>
<div class="abs press-badge" style="left:672px"><span></span></div>
<div class="abs press-badge" style="left:808px"><span></span></div>
<div class="abs press-badge" style="left:952px"><span></span></div>

<div class="abs divider" style="top:2072px"></div>

<footer>
  <div class="abs footer-col" style="left:109px">
    <h4>Buying on Gearcrate</h4>
    <ul><li>How It Works</li><li>Delivery</li><li>Returns</li><li>Contact The Seller</li><li>Buying FAQ</li></ul>
  </div>
  <div class="abs footer-col" style="left:304px">
    <h4>Gearcrate Community</h4>
    <ul><li>Gearcrate Forums</li><li>Blog</li><li>Selling On Gearcrate</li><li>Help &amp; Support</li></ul>
  </div>
  <div class="abs footer-col" style="left:501px">
    <h4>About Gearcrate</h4>
    <ul><li>Our Story</li><li>Contact Us</li><li>Privacy Policy</li><li>Terms Of Uses</li><li>Press Enquires</li></ul>
  </div>
  <div class="abs footer-col" style="left:689px">
    <h4>Subscribe To Our Weekly Email Guide</h4>
  </div>
  <div class="abs subscribe-input">Your email address</div>
  <div class="abs subscribe-btn">SUBSCRIBE</div>
  <div class="abs divider" style="left:650px;top:2205px;width:438px"></div>

  <div class="abs social" aria-label="Social links">
    <span style="background:#d2343a"></span><span style="background:#3c5a99"></span><span style="background:#3fa9e0"></span><span style="background:#3a3a3a"></span><span style="background:#3f5f7d"></span><span style="background:#ef4a2f"></span><span style="background:#404040"></span>
  </div>

  <div class="abs payments" aria-label="Accepted payment methods">
    <span class="top"></span>
    <div class="cards">
      <span style="background:#d33a2c"></span><span style="background:#f2f2f2"></span><span style="background:#d8333a"></span><span style="background:#5a8fd0"></span>
    </div>
  </div>

  <div class="abs copyright">Copyrights © 2014 Gearcrate.com - All Rights Reserved</div>
</footer>

</body>
</html>
```